Business Card Thorne Landscaping
Professional
Peter Thorne
P.O. Box 7634
Alder St.
Fernwick Valley 04318
peter@thornelandscaping.example
www.thornelandscaping.example
As a possibility it might be nice to incorporated the service we offer on the card they are Design / Build, Landscape Management, Turf and Snow. If this doesn't make the card not a big deal.
I would like to the see the option on the back of the card being green with just our logo in white or even just the symbol part of our logo.

```html
<!DOCTYPE html>
<html lang="en">
<head>
<meta charset="utf-8">
<title>Thorne Landscaping – Business Card</title>
<link rel="stylesheet" href="https://fonts.googleapis.com/css2?family=Arimo:wght@400;700&display=swap">
<style>
  :root {
    --brand-green: #1b6c3b;
    --card-white: #ffffff;
    --ink: #1a1a1a;
    --backdrop: #2a2a2a;
  }
  * { margin: 0; padding: 0; box-sizing: border-box; }
  html, body {
    width: 1200px;
    height: 826px;
    overflow: hidden;
    background: var(--backdrop);
    font-family: "Arimo", Arial, sans-serif;
  }
  .card {
    position: absolute;
    left: 120px;
    top: 137px;
    width: 960px;
    height: 552px;
    border-radius: 48px;
    overflow: hidden;
    background: var(--brand-green);
  }
  .card-face {
    position: absolute;
    inset: 0;
    width: 960px;
    height: 552px;
  }
  .brand {
    position: absolute;
    left: 150px;
    top: 40px;
    display: flex;
    align-items: center;
    gap: 20px;
  }
  .brand-dot {
    width: 100px;
    height: 100px;
    border-radius: 50%;
    background: var(--brand-green);
  }
  .brand-name {
    font-size: 46px;
    font-weight: 400;
    color: var(--brand-green);
    line-height: 1;
    white-space: nowrap;
  }
  .holder {
    position: absolute;
    right: 56px;
    top: 210px;
    text-align: right;
  }
  .holder-name {
    font-size: 33px;
    font-weight: 700;
    color: var(--brand-green);
    line-height: 1.1;
    white-space: nowrap;
  }
  .holder-title {
    font-size: 19px;
    color: var(--ink);
    margin-top: 4px;
  }
  .contact {
    position: absolute;
    left: 142px;
    top: 288px;
    list-style: none;
    font-size: 22px;
    line-height: 32px;
    color: var(--ink);
    white-space: nowrap;
  }
</style>
</head>
<body>
  <section class="card" aria-label="Thorne Landscaping business card">
    <svg class="card-face" viewBox="0 0 960 552" aria-hidden="true">
      <path d="M120 0 H960 V552 H108 C20 430 8 210 120 0 Z" fill="var(--card-white)"/>
    </svg>

    <div class="brand">
      <span class="brand-dot"></span>
      <span class="brand-name">Thorne Landscaping</span>
    </div>

    <div class="holder">
      <div class="holder-name">Peter Thorne</div>
      <div class="holder-title">President</div>
    </div>

    <ul class="contact">
      <li>P.O. Box 7634</li>
      <li>Alder St.</li>
      <li>Fernwick Valley 04318</li>
      <li>P : 207-555-0142</li>
      <li>F : 207-555-0187</li>
      <li>E : peter@thornelandscaping.example</li>
      <li>www.thornelandscaping.example</li>
    </ul>
  </section>
</body>
</html>
```